Flyer for the Lumen 2025 Conference

I am looking to produce a flyer for our upcoming conference, Lumen 2025. This is an annual conference that we plan to publicize on social media. The ideal designer will create a flyer that is eye-catching and effectively communicates the key information. Please see attached our logo, speaker photo, and flyer content.

Target Market(s)

All demographics

Industry/Entity Type

Christian

Font styles to use
Sans Serif

Requirements
Should not have
• Cross, church

```html
<!DOCTYPE html>
<html lang="en">
<head>
<meta charset="utf-8">
<title>Lumen 2025 Conference</title>
<link rel="stylesheet" href="https://fonts.googleapis.com/css2?family=Oswald:wght@400;600&family=Poppins:wght@300;400;500;600&family=Orbitron:wght@500&display=swap">
<style>
  :root {
    --navy: #123a66;
    --navy-deep: #0b2749;
    --navy-mid: #1c4d80;
    --orange: #f7941d;
    --white: #ffffff;
    --line: rgba(255,255,255,0.35);
  }
  * { box-sizing: border-box; margin: 0; padding: 0; }
  html, body { width: 1200px; height: 1200px; overflow: hidden; background: var(--navy); }
  .flyer {
    position: relative; width: 1200px; height: 1200px; overflow: hidden;
    font-family: 'Poppins', sans-serif; color: var(--white);
  }
  .backdrop {
    position: absolute; inset: 0;
    background: radial-gradient(ellipse at 75% 45%, #2a5d92 0%, var(--navy) 45%, var(--navy-deep) 100%);
  }
  .speaker-photo {
    position: absolute; left: 333px; top: 67px; width: 467px; height: 720px;
    background: linear-gradient(180deg, rgba(60,110,170,0.55) 0%, rgba(35,90,160,0.6) 50%, rgba(18,58,102,0) 100%);
    border-radius: 220px 220px 0 0;
  }
  .brand {
    position: absolute; left: 60px; top: 62px;
    font-family: 'Oswald', sans-serif; font-weight: 400; font-size: 50px;
    letter-spacing: 2px; color: var(--white);
  }
  .label { font-family: 'Poppins', sans-serif; font-weight: 300; font-size: 24px; color: var(--orange); }
  .speaker { position: absolute; left: 58px; top: 262px; }
  .speaker-name { font-family: 'Oswald', sans-serif; line-height: 1.05; margin-top: 6px; }
  .speaker-name .title { display: block; font-weight: 600; font-size: 45px; }
  .speaker-name .name { display: block; font-weight: 400; font-size: 40px; }
  .topic { position: absolute; right: 47px; top: 100px; text-align: right; }
  .topic-title { font-family: 'Oswald', sans-serif; line-height: 1.08; margin-top: 10px; }
  .topic-title .strong { display: block; font-weight: 600; font-size: 46px; }
  .topic-title .light { display: block; font-weight: 400; font-size: 46px; }
  .event-name {
    position: absolute; left: 0; width: 1200px; top: 530px; text-align: center;
    font-family: 'Orbitron', sans-serif; font-weight: 500; font-size: 112px;
    letter-spacing: 10px; color: var(--orange); line-height: 1;
  }
  .event-type {
    position: absolute; left: 0; width: 1200px; top: 664px; text-align: center;
    font-family: 'Orbitron', sans-serif; font-weight: 500; font-size: 54px;
    letter-spacing: 5px; color: var(--white); line-height: 1;
  }
  .schedule {
    position: absolute; left: 67px; top: 755px; width: 1071px;
    border-collapse: collapse; font-size: 21px;
  }
  .schedule th {
    background: var(--orange); color: var(--navy-deep); font-weight: 600;
    font-size: 21px; height: 56px; text-align: center;
  }
  .schedule td { height: 56px; border: 1px solid var(--line); background: rgba(11,39,73,0.55); }
  .schedule tr:last-child td { border-bottom-color: var(--orange); }
  .schedule .col-date { width: 370px; padding-left: 48px; }
  .schedule .col-time { width: 322px; text-align: center; }
  .schedule .venue {
    padding-left: 52px; font-size: 17px; line-height: 36px; text-transform: uppercase;
    border-bottom-color: var(--line);
  }
  .app-call { position: absolute; left: 292px; top: 1024px; font-size: 19px; }
  .download {
    position: absolute; left: 848px; top: 1011px; width: 290px; height: 53px;
    background: var(--white); color: var(--navy-deep); font-weight: 600; font-size: 20px;
    display: flex; align-items: center; justify-content: center; letter-spacing: 0.5px;
  }
  .divider { position: absolute; left: 0; top: 1094px; width: 1200px; height: 1px; background: var(--line); }
  .contact {
    position: absolute; top: 1128px; display: flex; align-items: center; gap: 12px;
    font-size: 25px; font-weight: 600;
  }
  .contact svg { width: 22px; height: 22px; }
  .contact-phone { left: 67px; }
  .contact-email { left: 445px; }
  .contact-web { left: 905px; }
</style>
</head>
<body>
<main class="flyer">
  <div class="backdrop" role="img" aria-label="Blurred photo of a conference audience in dark blue tones"></div>
  <div class="speaker-photo" role="img" aria-label="Photo of the speaker in a blue blazer"></div>

  <div class="brand">VERANE</div>

  <section class="speaker">
    <p class="label">Speaker:</p>
    <h2 class="speaker-name"><span class="title">PROPHET</span><span class="name">ELIAS MORENO</span></h2>
  </section>

  <section class="topic">
    <p class="label">Topic:</p>
    <h2 class="topic-title"><span class="strong">THE VOICE</span><span class="light">OF THE LORD</span></h2>
  </section>

  <h1 class="event-name">LUMEN 2025</h1>
  <p class="event-type">A PROPHETIC CONFERENCE</p>

  <table class="schedule">
    <thead>
      <tr><th>DATE</th><th>TIME</th><th>LOCATION</th></tr>
    </thead>
    <tbody>
      <tr>
        <td class="col-date">Friday, December 26th</td>
        <td class="col-time">6:30PM - 9:00PM</td>
        <td class="venue" rowspan="3">The Harborview Performing<br>Arts Center,<br>218 Linden Avenue,<br>Fairhaven, Maine 04110.</td>
      </tr>
      <tr>
        <td class="col-date">Saturday, December 27th</td>
        <td class="col-time">5:30PM - 8:00PM</td>
      </tr>
      <tr>
        <td class="col-date">Sunday, December 29th</td>
        <td class="col-time">4:30PM - 7:00PM</td>
      </tr>
    </tbody>
  </table>

  <p class="app-call">Download the VERANE App to stay updated on the event</p>
  <div class="download">DOWNLOAD NOW</div>

  <div class="divider"></div>

  <div class="contact contact-phone">
    <svg viewBox="0 0 24 24" aria-hidden="true"><path fill="#f7941d" d="M6.6 10.8a15.1 15.1 0 0 0 6.6 6.6l2.2-2.2c.3-.3.7-.4 1-.2 1.1.4 2.3.6 3.6.6.6 0 1 .4 1 1V20c0 .6-.4 1-1 1A17 17 0 0 1 3 4c0-.6.4-1 1-1h3.5c.6 0 1 .4 1 1 0 1.3.2 2.5.6 3.6.1.3 0 .7-.2 1z"/></svg>
    <span>207 555 0184</span>
  </div>
  <div class="contact contact-email">
    <svg viewBox="0 0 24 24" aria-hidden="true"><rect x="2" y="4" width="20" height="16" rx="2" fill="#f7941d"/><path d="M3 6l9 7 9-7" stroke="#123a66" stroke-width="2" fill="none"/></svg>
    <span>contact@verane.org</span>
  </div>
  <div class="contact contact-web">
    <svg viewBox="0 0 24 24" aria-hidden="true"><circle cx="12" cy="12" r="10" fill="#f7941d"/><path d="M2 12h20M12 2c3 3 3 17 0 20M12 2c-3 3-3 17 0 20" stroke="#123a66" stroke-width="1.5" fill="none"/></svg>
    <span>www.verane.org</span>
  </div>
</main>
</body>
</html>
```